Broschüren-Design für Produzent von hochwertigen Verpackungs- und Präsentationslösungen
Zielgruppe
Wir produzieren hochwertige Verpackungs- und Präsentationslösungen.
Unsere Zielgruppe sind Firmen, welche kreative Premium-Packaging benötigt.
Aufgabenstellung
- Format: A4 hoch
- Umfang: 6 Seiten
- Falzart: Wickelfalz
- Design muss sehr hochwertig sein. Passend zu unseren Produktion (siehe Bilder)
- Wir möchten mit diesem Falzprospekt eine Übersicht über unsere Produkte generieren.
- Die Produkte sind bereits schon hochwertig fotografiert und müssen in einem anspruchsvollen Design in Szene gesetzt werden.
- Der Prospekt sollte die Kunden emotional berühren.
- Auf der Titelseite werden wir den Titel «High Performance Packaging» mit Folien prägen
- Seitenaufbau gemäss meiner Visualisierung (im Anhang)
- Bei jeder Produktkategorie möchte ich ein Grosses Übersichtsbild zusammen mit einem kurzen Text.
Ergänzend können noch weitere (passende) Bilder der jeweiligen Kategorie abgebildet werden.
Im Anhang finden Sie:
- Visualisierung des zu gestaltenden Prospekt
- Werbeflyer (zur Ansicht/Inspiration). In etwa so stellen wir uns das Design/Tonalität vor.
- Weitere passende Produktbilder können vorerst auf der Webseite unseres Produktionspartner (www.bogenhaus.de) entnommen werden.

```html
<!DOCTYPE html>
<html lang="de">
<head>
<meta charset="utf-8">
<title>Kartova – Faltprospekt</title>
<link rel="stylesheet" href="https://fonts.googleapis.com/css2?family=Barlow:wght@300;400;600&family=Playfair+Display:ital,wght@1,900&display=swap">
<style>
  :root {
    --page: #ffffff;
    --slate: #404555;
    --copper: #c9784f;
    --ink: #111214;
    --white: #ffffff;
    --text-soft: #e4e6ec;
    --fold: #6d7283;
    --icon-bg: #eeeee8;
    --icon-green: #1f7a5a;
  }
  * { box-sizing: border-box; margin: 0; padding: 0; }
  html, body { width: 1015px; height: 1200px; overflow: hidden; background: var(--page); }
  body { position: relative; font-family: "Barlow", sans-serif; color: var(--white); }

  .brand-mark {
    position: absolute; top: 96px; left: 0; width: 1015px; text-align: center;
    font-weight: 600; font-size: 26px; color: var(--ink); letter-spacing: 0.5px;
  }

  .spread {
    position: absolute; left: 36px; width: 943px; height: 446px;
    box-shadow: 0 6px 22px rgba(0,0,0,0.16);
  }
  .spread--outside { top: 221px; background: var(--slate); overflow: hidden; }
  .spread--inside { top: 690px; background: var(--ink); overflow: hidden; }

  .fold { position: absolute; top: 8px; bottom: 8px; border-left: 1px dashed var(--fold); }
  .fold--one { left: 312px; }
  .fold--two { left: 627px; }

  .panel { position: absolute; top: 0; height: 446px; }
  .panel--inner-flap { left: 0; width: 312px; }
  .panel--back { left: 312px; width: 315px; }
  .panel--cover { left: 627px; width: 316px; overflow: hidden; }

  .intro { position: absolute; left: 53px; top: 66px; width: 188px; }
  .intro h2 { font-weight: 600; font-size: 8.6px; line-height: 1.35; margin-bottom: 6px; }
  .intro p { font-weight: 300; font-size: 6.6px; line-height: 1.36; color: var(--text-soft); margin-bottom: 5px; }
  .intro--sustain { top: 193px; }

  .features { position: absolute; left: 53px; top: 257px; width: 200px; list-style: none; }
  .feature { display: flex; align-items: flex-start; margin-bottom: 10px; height: 34px; }
  .feature-icon {
    flex: 0 0 33px; height: 33px; border-radius: 50%; background: var(--icon-bg);
    display: flex; align-items: center; justify-content: center; margin-right: 11px;
  }
  .feature-text { width: 145px; }
  .feature h3 { font-weight: 600; font-size: 7px; margin: 2px 0 5px; }
  .feature p { font-weight: 300; font-size: 6.6px; line-height: 1.36; color: var(--text-soft); }

  .contact { position: absolute; left: 205px; top: 400px; display: flex; gap: 5px; }
  .contact-name { font-weight: 600; font-size: 9px; line-height: 1; margin-top: 1px; }
  .contact-lines { font-size: 3.8px; line-height: 1.45; font-weight: 300; }
  .contact-lines strong { font-weight: 600; font-size: 4.2px; }
  .contact-lines .owner { margin-top: 3px; display: block; }

  .cover-brand { position: absolute; left: 146px; top: 22px; font-weight: 600; font-size: 8px; }
  .cover-title {
    position: absolute; left: 34px; top: 86px;
    font-family: "Playfair Display", serif; font-style: italic; font-weight: 900;
    font-size: 25px; line-height: 1.08; color: var(--copper);
  }
  .cover-sub { position: absolute; left: 34px; top: 172px; font-weight: 300; font-size: 8.6px; line-height: 1.3; color: var(--text-soft); }
  .cover-photo {
    position: absolute; left: 28px; top: 228px; width: 288px; height: 150px;
    background:
      radial-gradient(ellipse 60px 68px at 72px 68px, #7a5240 0%, #6a4636 60%, rgba(64,69,85,0) 100%),
      radial-gradient(ellipse 70px 30px at 150px 112px, #8d93a8 0%, #6f7487 55%, rgba(64,69,85,0) 100%),
      radial-gradient(ellipse 55px 40px at 150px 85px, #2c2f3a 0%, rgba(64,69,85,0) 100%),
      radial-gradient(ellipse 50px 40px at 262px 70px, #9aa0b4 0%, #4a4e5d 60%, rgba(64,69,85,0) 100%),
      radial-gradient(ellipse 150px 20px at 150px 138px, rgba(30,32,40,0.6) 0%, rgba(64,69,85,0) 100%);
  }

  .product { position: absolute; overflow: hidden; }
  .product-label { position: absolute; width: 72px; }
  .product-label h3 { font-weight: 600; font-size: 5.6px; margin-bottom: 4px; }
  .product-label p { font-weight: 300; font-size: 3.6px; line-height: 1.5; color: var(--text-soft); }

  .product--boxes { left: 0; top: 0; width: 315px; height: 147px;
    background:
      radial-gradient(ellipse 70px 28px at 180px 70px, #e9e9ea 0%, #bdbdc0 55%, rgba(40,40,43,0) 100%),
      radial-gradient(ellipse 50px 18px at 260px 48px, #cfcfd2 0%, rgba(40,40,43,0) 100%),
      radial-gradient(ellipse 60px 20px at 275px 100px, #55565b 0%, rgba(40,40,43,0) 100%),
      linear-gradient(135deg, #141416, #2b2b2e 55%, #1c1c1e); }
  .product--binder { left: 315px; top: 0; width: 315px; height: 147px;
    background:
      radial-gradient(ellipse 120px 55px at 110px 75px, #3fb4d0 0%, #2a8fa8 55%, rgba(55,58,64,0) 100%),
      radial-gradient(ellipse 55px 25px at 90px 55px, #f2f2f2 0%, rgba(55,58,64,0) 100%),
      radial-gradient(ellipse 65px 30px at 225px 30px, #1e2a36 0%, rgba(55,58,64,0) 100%),
      linear-gradient(150deg, #2c2f34, #3f4247 55%, #303236); }
  .product--fan { left: 630px; top: 0; width: 313px; height: 223px;
    background:
      radial-gradient(ellipse 70px 90px at 105px 110px, #9fa0a4 0%, #86878c 60%, rgba(94,94,116,0) 100%),
      radial-gradient(ellipse 80px 12px at 185px 205px, #a9aaae 0%, rgba(201,202,206,0) 100%),
      linear-gradient(180deg, #5e5e74 0%, #5e5e74 50%, #c9cace 51%, #e2e3e6 100%); }
  .product--presentation { left: 0; top: 147px; width: 315px; height: 151px;
    background:
      radial-gradient(ellipse 55px 30px at 55px 95px, #f1f1f1 0%, #cfcfd0 55%, rgba(40,40,42,0) 100%),
      radial-gradient(ellipse 110px 50px at 110px 85px, #3a3a3d 0%, rgba(40,40,42,0) 100%),
      radial-gradient(ellipse 80px 25px at 120px 25px, #3c3c3f 0%, rgba(40,40,42,0) 100%),
      linear-gradient(135deg, #1f1f21, #303033 60%, #262628); }
  .product--slipcase { left: 315px; top: 147px; width: 315px; height: 151px;
    background:
      radial-gradient(ellipse 35px 55px at 200px 55px, #1c1c1e 0%, #2b2b2e 60%, rgba(135,136,142,0) 100%),
      radial-gradient(ellipse 90px 25px at 195px 130px, #e6e6e8 0%, #bfc0c4 55%, rgba(135,136,142,0) 100%),
      radial-gradient(ellipse 40px 15px at 215px 140px, #b5a2b8 0%, rgba(135,136,142,0) 100%),
      linear-gradient(160deg, #7c7d83, #8e8f95 55%, #6b6c72); }
  .product--case { left: 630px; top: 223px; width: 313px; height: 223px;
    background:
      radial-gradient(ellipse 70px 55px at 110px 70px, #2e2e30 0%, rgba(20,20,22,0) 100%),
      radial-gradient(ellipse 90px 45px at 145px 155px, #232325 0%, #18181a 60%, rgba(20,20,22,0) 100%),
      radial-gradient(ellipse 55px 45px at 45px 185px, #2b2b2d 0%, rgba(20,20,22,0) 100%),
      linear-gradient(160deg, #0d0d0e, #1c1c1e 55%, #0b0b0c); }
  .product--sample { left: 0; top: 298px; width: 315px; height: 148px;
    background:
      radial-gradient(ellipse 55px 35px at 165px 110px, #f1f1f1 0%, #d0d0d1 55%, rgba(50,50,53,0) 100%),
      radial-gradient(ellipse 45px 25px at 285px 40px, #b79a82 0%, #8d7260 55%, rgba(50,50,53,0) 100%),
      radial-gradient(ellipse 50px 22px at 195px 25px, #222224 0%, rgba(50,50,53,0) 100%),
      linear-gradient(135deg, #38383b, #2b2b2e 60%, #48484b); }
  .product--writing { left: 315px; top: 298px; width: 315px; height: 148px;
    background:
      radial-gradient(ellipse 60px 32px at 145px 75px, #f3f3f3 0%, #d4d4d5 55%, rgba(60,60,64,0) 100%),
      radial-gradient(ellipse 60px 25px at 190px 35px, #4a4a4e 0%, rgba(60,60,64,0) 100%),
      radial-gradient(ellipse 110px 45px at 120px 95px, #1f1f21 0%, rgba(60,60,64,0) 100%),
      linear-gradient(145deg, #2a2a2c, #4d4d51 55%, #58585c); }
</style>
</head>
<body>

<div class="brand-mark">Kartova</div>

<section class="spread spread--outside">
  <div class="fold fold--one"></div>
  <div class="fold fold--two"></div>

  <div class="panel panel--inner-flap">
    <div class="intro">
      <h2>Höchste Qualität zu<br>unschlagbaren Preisen.</h2>
      <p>Mit einer unvergleichlich grossen Bandbreite im Bereich des Premium Packaging bieten wir vielseitige Verpackungs- und Präsentationslösungen.</p>
      <p>Einzigartiges Design, variable Formen und hochwertige Haptik unterstreichen die Bedeutung von Ihren Produkten.</p>
      <p>Überzeugen Sie sich jetzt und bestellen Sie<br>Ihr individuelles Angebot!</p>
    </div>
    <div class="intro intro--sustain">
      <h2>Nachhaltige Papiere<br>als Standard.</h2>
      <p>Bei uns gehen neuste Technologien und Umweltschutz Hand in Hand. Wir setzen auf nachhaltige Materialien und eine emissionsarme Produktion.</p>
    </div>
    <ul class="features">
      <li class="feature">
        <span class="feature-icon">
          <svg width="20" height="18" viewBox="0 0 20 18"><path d="M4 2 L8 12 H0 Z M10 0 L15 12 H5 Z M16 3 L20 12 H12 Z" fill="var(--icon-green)"/><rect x="0" y="14" width="20" height="1" fill="#555"/></svg>
        </span>
        <div class="feature-text"><h3>Nachhaltige Papiere</h3><p>Unsere Rohmaterialien stammen aus nachhaltiger Forstwirtschaft.</p></div>
      </li>
      <li class="feature">
        <span class="feature-icon">
          <svg width="16" height="19" viewBox="0 0 16 19"><path d="M8 0 L16 3 V9 C16 14 12 17 8 19 C4 17 0 14 0 9 V3 Z" fill="var(--icon-green)"/><path d="M4 9 L7 12 L12 5" stroke="#fff" stroke-width="1.8" fill="none"/></svg>
        </span>
        <div class="feature-text"><h3>Wiederverwendbarkeit</h3><p>Unsere Boxen sind so schön und stabil, dass man sie auf jeden Fall wiederverwendet.</p></div>
      </li>
      <li class="feature">
        <span class="feature-icon">
          <svg width="20" height="20" viewBox="0 0 20 20"><circle cx="10" cy="10" r="5" fill="var(--icon-green)"/><path d="M3 8 A7.5 7.5 0 0 1 16 5 M17 12 A7.5 7.5 0 0 1 4 15" stroke="#444" stroke-width="1.2" fill="none"/><path d="M16 2 V6 H12" stroke="#444" stroke-width="1.2" fill="none"/><path d="M4 18 V14 H8" stroke="#444" stroke-width="1.2" fill="none"/></svg>
        </span>
        <div class="feature-text"><h3>Recyclebare Lösungen</h3><p>Auf Nachfrage können wir Ihnen eine 100% recyclebare Verpackung anbieten.</p></div>
      </li>
    </ul>
  </div>

  <div class="panel panel--back">
    <div class="contact">
      <span class="contact-name">Kartova</span>
      <div class="contact-lines">
        <strong>kartova-pack.ch</strong><br>
        info@kartova-pack.ch<br>
        041 555 20 40
        <span class="owner">Eine Marke von FalterPresse</span>
      </div>
    </div>
  </div>

  <div class="panel panel--cover">
    <div class="cover-brand">Kartova</div>
    <h1 class="cover-title">High<br>Performance<br>Packaging</h1>
    <p class="cover-sub">Exklusive Verpackungs-<br>und Präsentationslösungen</p>
    <div class="cover-photo" role="img" aria-label="Produktfoto: kupferfarbener Schuber mit Schubladenbox und offener Schreibgeräte-Schachtel"></div>
  </div>
</section>

<section class="spread spread--inside">
  <div class="product product--boxes" role="img" aria-label="Produktfoto: weisse Klappschachtel mit Füller und Taschenmesser">
    <div class="product-label" style="left:19px;top:75px"><h3>Verpackungen.</h3><p>Edle Materialien und präzise Verarbeitung für Ihren Auftritt. Wir fertigen nach Mass, in kleinen wie grossen Auflagen, mit Prägung, Druck oder Veredelung ganz nach Wunsch.</p></div>
  </div>
  <div class="product product--binder" role="img" aria-label="Produktfoto: geöffneter Ringordner in Petrol mit Schuber">
    <div class="product-label" style="left:222px;top:75px"><h3>Ringordner.</h3><p>Edle Materialien und präzise Verarbeitung für Ihren Auftritt. Wir fertigen nach Mass, in kleinen wie grossen Auflagen, mit Prägung, Druck oder Veredelung ganz nach Wunsch.</p></div>
  </div>
  <div class="product product--fan" role="img" aria-label="Produktfoto: graue Fächermappe mit Registern">
    <div class="product-label" style="left:203px;top:35px"><h3>Fächermappen.</h3><p>Edle Materialien und präzise Verarbeitung für Ihren Auftritt. Wir fertigen nach Mass, in kleinen wie grossen Auflagen, mit Prägung, Druck oder Veredelung ganz nach Wunsch.</p></div>
  </div>
  <div class="product product--presentation" role="img" aria-label="Produktfoto: geöffnete schwarze Präsentationsmappe">
    <div class="product-label" style="left:222px;top:49px"><h3>Präsentationsmappen.</h3><p>Edle Materialien und präzise Verarbeitung für Ihren Auftritt. Wir fertigen nach Mass, in kleinen wie grossen Auflagen, mit Prägung, Druck oder Veredelung ganz nach Wunsch.</p></div>
  </div>
  <div class="product product--slipcase" role="img" aria-label="Produktfoto: Schuber mit drei Ordnern und Farbmusterblatt">
    <div class="product-label" style="left:36px;top:49px"><h3>Schuber.</h3><p>Edle Materialien und präzise Verarbeitung für Ihren Auftritt. Wir fertigen nach Mass, in kleinen wie grossen Auflagen, mit Prägung, Druck oder Veredelung ganz nach Wunsch.</p></div>
  </div>
  <div class="product product--case" role="img" aria-label="Produktfoto: schwarzer Präsentationskoffer mit Schaumstoffeinlage">
    <div class="product-label" style="left:203px;top:43px"><h3>Präsentationskoffer.</h3><p>Edle Materialien und präzise Verarbeitung für Ihren Auftritt. Wir fertigen nach Mass, in kleinen wie grossen Auflagen, mit Prägung, Druck oder Veredelung ganz nach Wunsch.</p></div>
  </div>
  <div class="product product--sample" role="img" aria-label="Produktfoto: Mustermappe mit Holzmustern">
    <div class="product-label" style="left:19px;top:18px"><h3>Mustermappen.</h3><p>Edle Materialien und präzise Verarbeitung für Ihren Auftritt. Wir fertigen nach Mass, in kleinen wie grossen Auflagen, mit Prägung, Druck oder Veredelung ganz nach Wunsch.</p></div>
  </div>
  <div class="product product--writing" role="img" aria-label="Produktfoto: geöffnete Schreibmappe mit Stift">
    <div class="product-label" style="left:222px;top:79px"><h3>Schreibmappen.</h3><p>Edle Materialien und präzise Verarbeitung für Ihren Auftritt. Wir fertigen nach Mass, in kleinen wie grossen Auflagen, mit Prägung, Druck oder Veredelung ganz nach Wunsch.</p></div>
  </div>
</section>

</body>
</html>
```